Dutch craft distillery needs labels designed for Gin bottle

We are a small craft distillery based in The Netherlands. We are currently producing only GIN. While we do have a logo for our distillery, we are still in search of a winning design for our Gin bottle. We are looking for something modern yet classy. Let your creativity run wild. Play around with colours, think out of the box….The winning designer will be challenged to create the coolest labels for the different flavours of Gin we will be producing in the near future. The label will maintain the same design elements throughout the design, but will also be able to differentiate each variety clearly. So for e.g. A flowery VosKamp Gin can have a pink label with a different description and a spicy VosKamp gin can have another colour with another description and so on. If the design really appeals to us, we might also invite the designer to do our website for us!

In a nutshell: It is a 500 ml bottle, (Please check the attachment so you get an idea as to what kind of bottle to imagine while making the labels). The bottle is going to have a light coloured wooden lid/cork to it. As of now we have a transparent seal to complete the sealing process once the bottling is done. The idea is that we will have two labels. One in the front and one behind. The size of the labels are as follows:

Front label: 102 x 76 mm the front label. (TO BE USED HORIZONTALLY). The details that we need on the front label are in a separate attachment.

Back label: The size for the label at the back of the bottle is: 76 x 51 mm (TO BE USED VERTICALLY) The information that needs to come on the label behind is also in the same document which is attached separately. The label behind will also have batch no. & date (Please refer to attachment to understand what I mean by batch no. date, distiller’s signature etc.) I have attached a picture of an already existing brand which has its batch number and distillers signature etc on it….so you can understand what I exactly mean by that. Please do not copy their design, this is purely to give you an idea as to what I mean by batch number and so on. The address of the distillery can be put horizontally, vertically, on the side along one border, or however you find appropriate. This is the address:
Berkenhoutlaan 41,
7311 KD, Hengelo.
The Netherlands.
www.voskamp.nl

Logo’s no drinking when pregnant, No driving and drinking, No drinking under the age of 18 need to be present on the label behind. Alternately, we can also have www.calm-sipping.com instead of the under 18 no alcohol sign, most alcohol bottles these days have it. Please let me know what else you would need from me for this. So be creative and do your best!

Thanks and regards, Marisol Venkataraghavan.

Target Market(s)

Largely males and females between 25-55 , the audience could even be slightly older.

Colors

Designer to choose colors to be used in the design.

Requirements
Must have
• 1) The labels need to be modern, yet classy, elite..
• 2) We need to specify the fact that we are a craft distillery and the gin is HANDMADE, using only the highest quality ingredients.
• 3) We at VosKamp live, breathe, dream, talk about our dream which is our distillery and its product. The label needs to bring home this point and should clearly specify and mention that it is produced and bottled in The Netherlands. Or handmade and bottled with love and passion in The Netherlands or something to that effect if it matches with the rest of the design.
• 4) The colours you chose must match in some way or the other with the colours used for the logo design.
Nice to have
• Would be nice to have colours and look bold, although not completely necessary.
Should not have
• What I definitely do not want is something too whacky like a skull or some kind of vague work of art. For the rest, I leave it upto you….!

```html
<!DOCTYPE html>
<html lang="en">
<head>
<meta charset="utf-8">
<title>VosKamp Gin – Front Label Variants</title>
<link rel="stylesheet" href="https://fonts.googleapis.com/css2?family=Rye&family=Old+Standard+TT:wght@400;700&family=Montserrat:wght@700;800&family=Playfair+Display:wght@700;900&display=swap">
<style>
  :root {
    --backdrop: #000000;
    --paper: #ebebe8;
    --paper-white: #ffffff;
    --navy: #2b2541;
    --orange: #ea773e;
    --ink-soft: #3a3550;
  }
  * { box-sizing: border-box; margin: 0; padding: 0; }
  html, body {
    width: 1200px; height: 900px; overflow: hidden;
    background: var(--backdrop);
  }
  .canvas { position: relative; width: 1200px; height: 900px; }

  .label {
    position: absolute; top: 408px;
    width: 316px; height: 262px;
    overflow: hidden;
  }
  .label--classic-navy   { left: 78px;  background: var(--paper); }
  .label--classic-orange { left: 442px; background: var(--paper); }
  .label--modern-band    { left: 812px; background: var(--paper-white); }

  .label__frame { position: absolute; inset: 0; }

  /* Classic label content */
  .classic {
    position: absolute; inset: 0;
    display: flex; flex-direction: column; align-items: center;
    color: var(--navy); font-family: "Old Standard TT", serif;
    padding-top: 26px;
  }
  .classic__claims {
    position: absolute; top: 44px; left: 36px; right: 36px;
    display: flex; justify-content: space-between;
    font-size: 6.5px; font-style: italic;
  }
  .classic__maker {
    font-family: "Rye", serif; font-size: 16px; color: var(--orange);
    letter-spacing: 0.5px; line-height: 1;
  }
  .classic__maker-sub {
    font-size: 8.5px; letter-spacing: 2px; font-weight: 700; margin-top: 2px;
  }
  .classic__name {
    font-family: "Rye", serif; font-size: 37px; line-height: 1;
    letter-spacing: 1px; margin-top: 10px;
  }
  .classic__gin {
    display: flex; align-items: center; gap: 8px;
    font-family: "Rye", serif; font-size: 24px; line-height: 1; margin-top: 2px;
  }
  .classic__gin::before, .classic__gin::after {
    content: ""; width: 44px; height: 3px; background: currentColor;
  }
  .classic__premium { font-size: 6.5px; letter-spacing: 1.5px; font-weight: 700; margin-top: 4px; }
  .classic__rule { width: 150px; height: 1px; background: var(--navy); margin-top: 2px; }
  .classic__bottler { font-size: 6.5px; letter-spacing: 0.6px; font-weight: 700; margin-top: 3px; }
  .classic__style { font-size: 16px; letter-spacing: 0.5px; margin-top: 4px; line-height: 1; }
  .classic__small-batch { font-size: 5.5px; letter-spacing: 0.8px; font-weight: 700; margin-top: 4px; }
  .classic__specs {
    display: flex; align-items: center; gap: 8px; margin-top: 10px;
    font-size: 6.5px;
  }
  .classic__specs .spec-box { border: 0.8px solid var(--navy); padding: 1px 3px; }
  .classic__specs .spec-oval {
    border: 0.8px solid var(--navy); border-radius: 50%;
    padding: 2px 6px; font-size: 4.5px; text-align: center; line-height: 1.1;
  }

  .label--classic-navy .classic__name,
  .label--classic-navy .classic__gin { color: var(--navy); }
  .label--classic-navy .classic__style { color: var(--orange); }
  .label--classic-orange .classic__name,
  .label--classic-orange .classic__gin { color: var(--orange); }
  .label--classic-orange .classic__style { color: var(--navy); }

  /* Modern label content */
  .modern__band { position: absolute; inset: 0; }
  .modern__badge { position: absolute; left: 48px; top: 4px; width: 220px; height: 130px; }
  .modern__text {
    position: absolute; left: 0; right: 0; top: 150px;
    display: flex; flex-direction: column; align-items: center;
    color: var(--paper-white);
  }
  .modern__style {
    font-family: "Montserrat", sans-serif; font-weight: 800;
    font-size: 17px; letter-spacing: 1px; line-height: 1;
  }
  .modern__claims {
    font-family: "Old Standard TT", serif; font-weight: 700;
    font-size: 6.5px; letter-spacing: 0.6px; margin-top: 8px; text-align: center; line-height: 1.3;
  }
  .modern__rule { width: 270px; height: 1px; background: var(--paper-white); margin-top: 10px; }
  .modern__specs {
    width: 286px; display: flex; justify-content: space-between;
    font-family: "Old Standard TT", serif; font-weight: 700;
    font-size: 10px; margin-top: 5px;
  }
</style>
</head>
<body>
<main class="canvas">

  <!-- Variant A: navy name, orange style line -->
  <section class="label label--classic-navy">
    <svg class="label__frame" viewBox="0 0 316 262" fill="none" stroke="#2b2541">
      <path d="M10 60 V10 H100" stroke-width="2"/>
      <path d="M15 60 V15 H100" stroke-width="0.8"/>
      <path d="M306 60 V10 H216" stroke-width="2"/>
      <path d="M301 60 V15 H216" stroke-width="0.8"/>
      <path d="M10 202 V252 H100" stroke-width="2"/>
      <path d="M15 202 V247 H100" stroke-width="0.8"/>
      <path d="M306 202 V252 H216" stroke-width="2"/>
      <path d="M301 202 V247 H216" stroke-width="0.8"/>
      <path d="M20 95 V170 M296 95 V170" stroke-width="1"/>
    </svg>
    <div class="classic">
      <div class="classic__claims"><span>100% Natural Botanicals</span><span>No Artificial Flavouring</span></div>
      <div class="classic__maker">VOSKAMP</div>
      <div class="classic__maker-sub">DISTILLERY</div>
      <div class="classic__name">VOSKAMP</div>
      <div class="classic__gin">GIN</div>
      <div class="classic__premium">PREMIUM</div>
      <div class="classic__rule"></div>
      <div class="classic__bottler">DISTILLED AND BOTTLED BY VOSKAMP DISTILLERY</div>
      <div class="classic__style">LONDON DRY GIN</div>
      <div class="classic__small-batch">HANDCRAFTED IN SMALL BATCH</div>
      <div class="classic__specs">
        <span class="spec-box">50 CL|43% ALC.</span>
        <span class="spec-oval">PRODUCT OF<br>NETHERLANDS</span>
        <span>VOL. 500 ML</span>
      </div>
    </div>
  </section>

  <!-- Variant B: orange name, navy style line -->
  <section class="label label--classic-orange">
    <svg class="label__frame" viewBox="0 0 316 262" fill="none" stroke="#2b2541">
      <path d="M10 60 V10 H100" stroke-width="2"/>
      <path d="M15 60 V15 H100" stroke-width="0.8"/>
      <path d="M306 60 V10 H216" stroke-width="2"/>
      <path d="M301 60 V15 H216" stroke-width="0.8"/>
      <path d="M10 202 V252 H100" stroke-width="2"/>
      <path d="M15 202 V247 H100" stroke-width="0.8"/>
      <path d="M306 202 V252 H216" stroke-width="2"/>
      <path d="M301 202 V247 H216" stroke-width="0.8"/>
      <path d="M20 95 V170 M296 95 V170" stroke-width="1"/>
    </svg>
    <div class="classic">
      <div class="classic__claims"><span>100% Natural Botanicals</span><span>No Artificial Flavouring</span></div>
      <div class="classic__maker">VOSKAMP</div>
      <div class="classic__maker-sub">DISTILLERY</div>
      <div class="classic__name">VOSKAMP</div>
      <div class="classic__gin">GIN</div>
      <div class="classic__premium">PREMIUM</div>
      <div class="classic__rule"></div>
      <div class="classic__bottler">DISTILLED AND BOTTLED BY VOSKAMP DISTILLERY</div>
      <div class="classic__style">LONDON DRY GIN</div>
      <div class="classic__small-batch">HANDCRAFTED IN SMALL BATCH</div>
      <div class="classic__specs">
        <span class="spec-box">50 CL|43% ALC.</span>
        <span class="spec-oval">PRODUCT OF<br>NETHERLANDS</span>
        <span>VOL. 500 ML</span>
      </div>
    </div>
  </section>

  <!-- Variant C: navy sweep with ribbon badge -->
  <section class="label label--modern-band">
    <svg class="modern__band" viewBox="0 0 316 262">
      <path d="M0 120 Q170 105 316 8 V262 H0 Z" fill="#2b2541"/>
    </svg>
    <svg class="modern__badge" viewBox="0 0 220 130">
      <defs>
        <path id="badge-arc" d="M62 78 A48 48 0 0 0 158 78"/>
      </defs>
      <circle cx="110" cy="58" r="54" fill="#ffffff" stroke="#2b2541" stroke-width="1.5"/>
      <circle cx="110" cy="58" r="50" fill="none" stroke="#2b2541" stroke-width="0.6"/>
      <text x="110" y="32" text-anchor="middle" font-family="Rye, serif" font-size="13" fill="#ea773e">VOSKAMP</text>
      <text x="110" y="43" text-anchor="middle" font-family="Old Standard TT, serif" font-weight="700" font-size="7" letter-spacing="1.5" fill="#2b2541">DISTILLERY</text>
      <path d="M10 48 H210 L202 64 L210 80 H10 L18 64 Z" fill="#ffffff" stroke="#2b2541" stroke-width="1.5"/>
      <path d="M22 52 H198 V76 H22 Z" fill="none" stroke="#2b2541" stroke-width="0.6"/>
      <text x="110" y="73" text-anchor="middle" font-family="Playfair Display, serif" font-weight="900" font-size="22" fill="#2b2541">VOSKAMP GIN</text>
      <text x="110" y="92" text-anchor="middle" font-family="Old Standard TT, serif" font-weight="700" font-size="7" letter-spacing="1.5" fill="#2b2541">PREMIUM</text>
      <text font-family="Old Standard TT, serif" font-weight="700" font-size="5.5" letter-spacing="0.8" fill="#2b2541">
        <textPath href="#badge-arc" startOffset="50%" text-anchor="middle">HANDCRAFTED IN SMALL BATCH</textPath>
      </text>
    </svg>
    <div class="modern__text">
      <div class="modern__style">LONDON DRY GIN</div>
      <div class="modern__claims">100% NATURAL BOTANICALS ● NO ARTIFICIAL FLAVOURING<br>DISTILLED AND BOTTLED BY VOSKAMP DISTILLERY</div>
      <div class="modern__rule"></div>
      <div class="modern__specs"><span>50 CL|43% ALC.</span><span>PRODUCT OF NETHERLANDS</span><span>VOL. 500 ML</span></div>
    </div>
  </section>

</main>
</body>
</html>
```